Website Design for A Leading Live Casino Software Provider

We provide live casino software to other land based and online gaming establishments. We are a B2B provider.

```html
<!DOCTYPE html>
<html lang="en">
<head>
<meta charset="utf-8">
<title>Apex Table Studios – Live Casino Software</title>
<link rel="stylesheet" href="https://fonts.googleapis.com/css2?family=Arimo:wght@400;700&family=Bebas+Neue&family=Oswald:wght@500;600&display=swap">
<style>
:root{
  --page:#f2f2f2;
  --navy:#0d3c73;
  --blue:#1a5ea6;
  --blue-dark:#0e4a8c;
  --blue-light:#3a82c8;
  --panel:#ffffff;
  --frame:#e3e3e3;
  --line:#d8d8d8;
  --text:#333333;
  --muted:#555555;
  --link:#0d3c73;
  --orange:#e69516;
  --orange-dark:#d57f0b;
  --cream:#fff7e2;
  --banner-sub:#4a2a05;
}
*{box-sizing:border-box;margin:0;padding:0}
html,body{width:880px;height:1200px;overflow:hidden}
body{
  position:relative;
  background:var(--page);
  font-family:"Arimo",Arial,sans-serif;
  color:var(--text);
}
.abs{position:absolute}

/* header */
.brand{left:39px;top:28px;display:flex;align-items:center;gap:8px}
.brand-mark{width:34px;height:34px;border-radius:50%;background:var(--blue)}
.brand-name{font-weight:700;font-size:19px;color:var(--navy);letter-spacing:.5px;line-height:1.05}
.search{left:593px;top:41px;display:flex}
.search-input{width:198px;height:26px;background:#fff;border:1px solid #d6d6d6}
.search-btn{width:46px;height:26px;margin-left:2px;background:linear-gradient(var(--blue-light),var(--blue-dark));color:#fff;font-size:10px;display:flex;align-items:center;justify-content:center}

/* navigation */
.nav{left:0;top:108px;width:880px;height:85px;background:linear-gradient(var(--blue-light) 0%,var(--blue) 45%,var(--blue-dark) 100%);border-bottom:1px solid #0a3a70}
.nav-list{position:absolute;left:41px;top:0;display:flex;list-style:none;height:85px}
.nav-item{width:94px;height:85px;border-right:1px solid #0b3f7a;box-shadow:inset -1px 0 0 rgba(255,255,255,.18);display:flex;flex-direction:column;align-items:center;justify-content:flex-end;padding-bottom:10px;color:#fff;font-size:9px;font-weight:700;letter-spacing:.2px;white-space:nowrap}
.nav-item svg{width:34px;height:34px;margin-bottom:13px}
.nav-item.is-active{background:linear-gradient(#ffffff,#d9d9d9);color:var(--navy)}

/* hero slider */
.hero{left:40px;top:217px;width:800px;height:375px;background:var(--frame);border:1px solid #d3d3d3}
.hero-image{position:absolute;left:12px;top:12px;width:775px;height:324px;background:radial-gradient(ellipse at 72% 75%,#c9a040 0%,#8a4b1e 30%,#5a2a12 55%,#2a1408 100%)}
.hero-caption{position:absolute;left:16px;top:234px;width:380px;height:78px;background:rgba(30,30,30,.72);padding:12px 16px}
.hero-title{font-family:"Bebas Neue",sans-serif;font-weight:400;font-size:24px;color:#fff;letter-spacing:.3px;line-height:1}
.hero-text{font-size:10px;color:#e6e6e6;line-height:14px;margin-top:6px}
.hero-dots{position:absolute;left:0;right:0;top:355px;display:flex;justify-content:center;gap:6px}
.dot{width:14px;height:14px;border-radius:50%;background:#fff;border:1px solid #c8c8c8}
.dot.is-current{background:var(--navy);border-color:var(--navy)}

/* dealers */
.dealers{left:40px;top:617px;width:536px;height:300px;background:var(--panel);border:1px solid var(--line)}
.section-title{font-family:"Bebas Neue",sans-serif;font-weight:400;font-size:22px;color:var(--navy);position:absolute;left:14px;top:12px;letter-spacing:.2px;white-space:nowrap}
.section-sub{position:absolute;left:15px;top:38px;font-size:10px;color:#333;white-space:nowrap}
.dealer-card{position:absolute;background:#dedede;border:2px solid #eeeeee;outline:1px solid #d0d0d0}
.dealer-arrow{position:absolute;top:160px;width:24px;height:26px;background:#e2e2e2;display:flex;align-items:center;justify-content:center}
.dealer-arrow svg{width:10px;height:14px}

/* news */
.news{left:600px;top:617px;width:240px;height:251px;background:var(--panel);border:1px solid var(--line);overflow:hidden}
.tabs{display:flex;height:40px;margin:-1px -1px 0 -1px;background:var(--page);border-bottom:1px solid var(--line)}
.tab{font-size:10px;font-weight:700;color:#111;display:flex;align-items:center;padding:0 14px;height:40px;white-space:nowrap}
.tab.is-active{background:#fff;border:1px solid var(--line);border-bottom:none;height:41px;padding-bottom:1px}
.news-list{list-style:none;padding:6px 15px 0}
.news-item{padding:8px 0 6px;border-bottom:1px dashed #d5d5d5}
.news-item:last-child{border-bottom:none}
.news-title{font-size:8.6px;color:var(--link);line-height:12px;white-space:nowrap}
.news-date{font-size:8.6px;color:#444;line-height:12px}

/* call banner */
.call{left:40px;top:942px;width:536px;height:85px;background:linear-gradient(#f1aa22,var(--orange) 50%,var(--orange-dark));border:1px solid #c97a0a;text-align:center;padding-top:10px}
.call-main{font-family:"Oswald",sans-serif;font-weight:600;font-size:30px;line-height:34px;color:var(--cream);white-space:nowrap}
.call-sub{font-family:"Oswald",sans-serif;font-weight:500;font-size:19px;line-height:24px;color:var(--banner-sub);white-space:nowrap}

/* footer */
.about{left:40px;top:1051px;width:800px;height:67px;background:#dcdcdc;padding:13px 15px;font-size:9px;line-height:14px;color:#444}
.about a{color:#333;text-decoration:underline}
.legal{left:56px;top:1140px;width:770px;display:flex;justify-content:space-between;font-size:10px;color:#444}
.legal-links a{color:#444;text-decoration:none}
.legal-links span{margin:0 4px}
</style>
</head>
<body>

<header>
  <div class="abs brand">
    <span class="brand-mark"></span>
    <span class="brand-name">ATS<br>Apex Table Studios</span>
  </div>
  <div class="abs search">
    <div class="search-input"></div>
    <div class="search-btn">Search</div>
  </div>
</header>

<nav class="abs nav">
  <ul class="nav-list">
    <li class="nav-item is-active">
      <svg viewBox="0 0 34 34"><path d="M17 4 3 16h4v14h8v-9h4v9h8V16h4z" fill="#0d3c73"/></svg>HOME</li>
    <li class="nav-item">
      <svg viewBox="0 0 34 34"><path d="M17 3C12 10 5 14 5 20a6 6 0 0 0 10 4l-2 7h8l-2-7a6 6 0 0 0 10-4c0-6-7-10-12-17z" fill="#fff"/></svg>LIVE GAMES</li>
    <li class="nav-item">
      <svg viewBox="0 0 34 34"><circle cx="17" cy="17" r="10" fill="none" stroke="#fff" stroke-width="6" stroke-dasharray="5 3.4"/><circle cx="17" cy="17" r="8" fill="none" stroke="#fff" stroke-width="3"/></svg>OUR SOLUTIONS</li>
    <li class="nav-item">
      <svg viewBox="0 0 34 34"><circle cx="17" cy="17" r="14" fill="none" stroke="#fff" stroke-width="3"/><path d="M13 10v14l11-7z" fill="#fff"/></svg>VIDEOS</li>
    <li class="nav-item">
      <svg viewBox="0 0 34 34"><path d="M4 13h6l14-8v24L10 21H4z" fill="none" stroke="#fff" stroke-width="2.6"/><path d="M8 21l2 8h4l-2-8" fill="#fff"/><path d="M28 13v8" stroke="#fff" stroke-width="3"/></svg>NEWS &amp; EVENTS</li>
    <li class="nav-item">
      <svg viewBox="0 0 34 34"><circle cx="17" cy="10" r="6" fill="#fff"/><path d="M6 31c0-8 4-13 11-13s11 5 11 13z" fill="#fff"/></svg>ABOUT US</li>
    <li class="nav-item">
      <svg viewBox="0 0 34 34"><circle cx="17" cy="17" r="14" fill="none" stroke="#fff" stroke-width="3"/><text x="17" y="23" font-size="17" font-weight="700" text-anchor="middle" fill="#fff" font-family="Arimo,Arial,sans-serif">@</text></svg>CONTACT US</li>
  </ul>
</nav>

<section class="abs hero">
  <div class="hero-image" role="img" aria-label="Close-up photo of a spinning roulette wheel with golden turret and white ball"></div>
  <div class="hero-image" style="background:none">
    <div class="hero-caption">
      <h2 class="hero-title">EASY TO INTEGRATE, FLEXIBLE SOLUTIONS</h2>
      <p class="hero-text">We will work with you to ensure a smooth integration and provide a service that fits your needs.</p>
    </div>
  </div>
  <div class="hero-dots">
    <span class="dot"></span><span class="dot"></span><span class="dot is-current"></span><span class="dot"></span><span class="dot"></span>
  </div>
</section>

<section class="abs dealers">
  <h2 class="section-title">GET TO KNOW OUR BEAUTIFUL DEALERS</h2>
  <p class="section-sub">They Will Ensure Your Players are Smiling Even when Losing!</p>
  <div class="dealer-arrow" style="left:0"><svg viewBox="0 0 10 14"><path d="M8 1 2 7l6 6" fill="none" stroke="#0d3c73" stroke-width="2"/></svg></div>
  <div class="dealer-card" style="left:50px;top:116px;width:104px;height:112px"></div>
  <div class="dealer-card" style="left:180px;top:72px;width:186px;height:200px"></div>
  <div class="dealer-card" style="left:392px;top:116px;width:104px;height:112px"></div>
  <div class="dealer-arrow" style="right:0"><svg viewBox="0 0 10 14"><path d="M2 1l6 6-6 6" fill="none" stroke="#0d3c73" stroke-width="2"/></svg></div>
</section>

<aside class="abs news">
  <div class="tabs">
    <div class="tab is-active">LATEST NEWS</div>
    <div class="tab">LATEST EVENTS</div>
  </div>
  <ul class="news-list">
    <li class="news-item"><p class="news-title">ATS featured in TES Latin America 2011 in Panama</p><p class="news-date">2011.03.09</p></li>
    <li class="news-item"><p class="news-title">15 units of kiosk delivered to Mexico</p><p class="news-date">2010.06.12</p></li>
    <li class="news-item"><p class="news-title">"SILVER ACE" set to implement Live Dealer product</p><p class="news-date">2010.05.10</p></li>
    <li class="news-item"><p class="news-title">New High Definition video equipment placed in studio</p><p class="news-date">2010.05.06</p></li>
    <li class="news-item"><p class="news-title">Hours of operation extended</p><p class="news-date">2010.04.26</p></li>
  </ul>
</aside>

<section class="abs call">
  <p class="call-main">Call Toll Free 1-800-555-0142</p>
  <p class="call-sub">and get a FREE Demo of our Software and Solutions</p>
</section>

<footer>
  <p class="abs about">Apex Table Studios is a leader among <a>online casino software providers</a>. Our team of expert <a>internet casino software developers</a>, managers and marketers are here to ensure that any project you need, is a project Apex Table Studios can deliver. Our Casino services and consulting solutions can take your business to the next level. Our <a>online casino software licensing</a> can help any start up achieve the quickest and most secure return on investment.</p>
  <div class="abs legal">
    <span>Copyright © 2011, Apex Table Studios, All Rights Reserved.</span>
    <span class="legal-links"><a>Home</a><span>|</span><a>Terms &amp; Conditions</a><span>|</span><a>Privacy Policy</a></span>
  </div>
</footer>

</body>
</html>
```